Designing the poster for an original Broadway-style musical

We need a poster design for the original children's musical, MOSS PETAL AND THE JUMPING GNOMES. The had avery successful run and it is now being published. This poster/graphic design will be used for the publication cover as well as the poster for future productions. The design needs to incorporate the title: MOSS PETAL AND THE JUMPING GNOMES. It must also include: Book by Tod Varga, Music by Ulric Penhall, and Lyrics by Marisol Varga. It should be a Broadway caliber design.

Target Market(s)

Theatre Producers, Theatre audiences

Industry/Entity Type

Entertainment

Requirements
Must have
• MOSS PETAL AND THE JUMPING GNOMES
• Book by Tod Varga, Music by Ulric Penhall, Lyrics by Marisol Varga
Nice to have
• Colorful, bright, energetic.
Should not have
• No Halvern figures. As seen in our photos... our Moss Petal resembles Halvern's but is our own.

```html
<!DOCTYPE html>
<html lang="en">
<head>
<meta charset="utf-8">
<title>Moss Petal and the Jumping Gnomes — Poster</title>
<link rel="stylesheet" href="https://fonts.googleapis.com/css2?family=Kaushan+Script&family=Roboto+Condensed:wght@400;700&display=swap">
<style>
  :root {
    --page-bg: #e4e4e2;
    --sky-blue: #8fa9c6;
    --haze: #c9d3de;
    --teal: #1b8fb8;
    --magenta: #d3267c;
    --violet: #5a2f8a;
    --amber: #e0a33a;
    --green: #2f9e6e;
    --shadow-plum: #2a1530;
    --type-white: #ffffff;
  }
  * { margin: 0; padding: 0; box-sizing: border-box; }
  html, body {
    width: 1200px;
    height: 1200px;
    overflow: hidden;
    background: var(--page-bg);
  }
  .poster {
    position: absolute;
    left: 231px;
    top: 30px;
    width: 737px;
    height: 1140px;
    overflow: hidden;
    background: var(--sky-blue);
  }
  .poster__artwork {
    position: absolute;
    inset: 0;
    background:
      radial-gradient(ellipse 40% 30% at 15% 20%, rgba(211,38,124,0.75), transparent 70%),
      radial-gradient(ellipse 35% 25% at 30% 8%, rgba(224,163,58,0.8), transparent 70%),
      radial-gradient(ellipse 45% 35% at 20% 48%, rgba(27,143,184,0.85), transparent 70%),
      radial-gradient(ellipse 30% 30% at 95% 55%, rgba(47,158,110,0.7), transparent 70%),
      radial-gradient(ellipse 45% 30% at 85% 85%, rgba(211,38,124,0.8), transparent 70%),
      radial-gradient(ellipse 40% 25% at 10% 75%, rgba(90,47,138,0.55), transparent 70%),
      linear-gradient(180deg, var(--sky-blue) 0%, var(--haze) 85%, #dfe4ea 100%);
  }
  .poster__dancers {
    position: absolute;
    left: 150px;
    top: 620px;
    width: 500px;
    height: 520px;
    background: radial-gradient(ellipse 50% 50% at 50% 50%, rgba(42,21,48,0.85), rgba(90,47,138,0.55) 55%, transparent 80%);
  }
  .title {
    position: absolute;
    inset: 0;
    font-family: "Kaushan Script", cursive;
    color: var(--type-white);
    line-height: 1;
  }
  .title__line { position: absolute; white-space: nowrap; }
  .title__line--moss   { left: 142px; top: 80px;  font-size: 180px; transform: rotate(-4deg); }
  .title__line--petal  { left: 250px; top: 282px; font-size: 92px; }
  .title__line--the    { left: 295px; top: 362px; font-size: 92px; }
  .title__line--jumping{ left: 215px; top: 448px; font-size: 88px; }
  .title__line--gnomes { left: 235px; top: 535px; font-size: 96px; }
  .credits {
    position: absolute;
    left: 0;
    right: 0;
    top: 1068px;
    text-align: center;
    font-family: "Roboto Condensed", sans-serif;
    color: var(--type-white);
  }
  .credits__book {
    font-weight: 700;
    font-size: 27px;
    letter-spacing: 0.3em;
    padding-left: 0.3em;
  }
  .credits__team {
    margin-top: 6px;
    font-weight: 400;
    font-size: 15px;
    letter-spacing: 0.01em;
  }
</style>
</head>
<body>
  <main class="poster">
    <div class="poster__artwork" role="img" aria-label="Bursts of coloured powder paint in magenta, teal, amber and green over a pale blue sky with sparkling lights"></div>
    <div class="poster__dancers" role="img" aria-label="Silhouettes of two dancers back to back, one raising their arms, one holding a fan and sweeping a long skirt"></div>

    <h1 class="title" aria-label="Moss Petal and the Jumping Gnomes">
      <span class="title__line title__line--moss">Moss</span>
      <span class="title__line title__line--petal">Petal&amp;</span>
      <span class="title__line title__line--the">The</span>
      <span class="title__line title__line--jumping">Jumping</span>
      <span class="title__line title__line--gnomes">Gnomes</span>
    </h1>

    <footer class="credits">
      <p class="credits__book">BOOK BY TOD VARGA</p>
      <p class="credits__team">MUSIC BY ULRIC PENHALL &nbsp;|&nbsp; LYRICS BY MARISOL VARGA.</p>
    </footer>
  </main>
</body>
</html>
```